Web Homepage and logo for a sculptured cake and chocolate business

Taking its influence and inspiration from the 18th century artistic movement and style my business "Velvetrufflia" combines witty, artistic themes, ornate and whimsical designs with refined tastes to create fanciful, always extravagant and truly luscious sculptured cakes and chocolate creations using the finest quality chocolate sourced from across the world.
I will be selling bespoke cakes and chocolate creations on line and require a logo and website homepage that represents the extravagant, rich and sumptuous colours of the rococo period. As an example my multi layed cake creations could extend from outrageous gothic style weddings, elaborate 6 tier floral weddings, corporate representative sculptures, themed adult and childrens birthdays and exquisite individual chocolates for special occasions such as Easter, Valentines day and Christmas.
Updates

Hi everyone,

It would appear I need to clarify a couple of things. As my brief stated the name of my business is Velvetrufflia. If you use a textual logo it must use this name however if you do a non textual image it is fine as long as the name appears on the website.

If you want to use some content on the website then I would suggest something like the following (which comes from my brief). My intention is to play around with this once I have the logo and homepage designs
Velvetrufflia combines witty, artistic themes, ornate and whimsical designs with refined tastes to create a fanciful and truly luscious scultured cakes and chocolate creations using the finest quality chocolate sourced from across the world

I hope this helps and look forward to your designs.

Industry/Entity Type

Floral

```html
<!DOCTYPE html>
<html lang="en">
<head>
<meta charset="utf-8">
<title>Velvetrufflia – Cakes</title>
<link rel="stylesheet" href="https://fonts.googleapis.com/css2?family=Great+Vibes&family=Josefin+Sans:wght@300&display=swap">
<style>
  :root {
    --cream: #fdf8de;
    --stripe: #f8f0b8;
    --lavender: #d6c3e0;
    --chocolate: #3f2b29;
    --chocolate-soft: #4a3431;
    --plum: #6e3a6e;
    --label: #fbf6e4;
    --nav-text: #f4ebdc;
  }
  html, body {
    margin: 0;
    padding: 0;
    overflow: hidden;
  }
  .page {
    position: relative;
    width: 1200px;
    height: 970px;
    overflow: hidden;
    background: linear-gradient(to bottom, var(--cream) 246px, #f6efe0 520px, var(--lavender) 970px);
  }
  .header-band {
    position: absolute;
    left: 0; top: 0;
    width: 1200px;
    height: 245px;
    background: repeating-linear-gradient(-60deg, var(--cream) 0 10px, var(--stripe) 10px 20px);
  }
  .header-rule {
    position: absolute;
    left: 0; top: 244px;
    width: 1200px;
    height: 3px;
    background: var(--plum);
  }
  .page-title {
    position: absolute;
    right: 72px;
    top: 58px;
    margin: 0;
    font-family: "Great Vibes", cursive;
    font-weight: 400;
    font-size: 128px;
    line-height: 1.2;
    color: var(--plum);
  }
  .ribbon-stripes {
    position: absolute;
    left: 168px; top: 0;
    width: 142px;
    height: 180px;
    background: repeating-linear-gradient(-70deg, var(--chocolate) 0 6px, var(--cream) 6px 11px);
  }
  .sidebar {
    position: absolute;
    left: 168px; top: 300px;
    width: 142px;
    height: 670px;
    background: var(--chocolate);
  }
  .flourish {
    position: absolute;
    background: linear-gradient(160deg, var(--chocolate-soft), var(--chocolate));
  }
  .flourish--top {
    left: 0; top: 0;
    width: 165px; height: 225px;
    border-radius: 0 0 120px 0;
  }
  .flourish--bottom {
    left: 1020px; top: 815px;
    width: 180px; height: 155px;
    border-radius: 120px 0 0 0;
  }
  .brand-label {
    position: absolute;
    left: 63px; top: 160px;
    width: 355px; height: 168px;
    box-sizing: border-box;
    background: var(--label);
    border: 5px solid var(--chocolate);
    border-radius: 40px;
    box-shadow: inset 0 0 0 5px var(--label), inset 0 0 0 6px var(--chocolate);
    display: flex;
    align-items: center;
    justify-content: center;
  }
  .brand-name {
    margin: 0;
    font-family: "Great Vibes", cursive;
    font-weight: 400;
    font-size: 62px;
    line-height: 1;
    color: var(--plum);
  }
  .main-nav {
    position: absolute;
    left: 193px; top: 354px;
  }
  .main-nav ul {
    list-style: none;
    margin: 0;
    padding: 0;
  }
  .main-nav li {
    height: 55px;
  }
  .main-nav a {
    font-family: "Josefin Sans", sans-serif;
    font-weight: 300;
    font-size: 25px;
    color: var(--nav-text);
    text-decoration: none;
  }
  .cake-gallery {
    position: absolute;
    left: 439px; top: 364px;
    display: grid;
    grid-template-columns: repeat(3, 189px);
    grid-auto-rows: 189px;
    column-gap: 32px;
    row-gap: 52px;
  }
  .cake-photo {
    box-sizing: border-box;
    border: 1.5px solid #5a2e22;
  }
  .cake-photo--fireside { background: linear-gradient(to bottom, #2a0c02 0%, #b8560e 35%, #3a2418 65%, #f2ece6 88%, #5a4a44 100%); }
  .cake-photo--walnut   { background: radial-gradient(circle at 50% 45%, #4a2418 0 55%, #c9a48a 70%, #8a6a5a 100%); }
  .cake-photo--marzipan { background: radial-gradient(circle at 50% 50%, #f2e2b4 0 55%, #d8c6a8 70%, #9a8a84 100%); }
  .cake-photo--layered  { background: radial-gradient(circle at 55% 45%, #a86a44 0 45%, #c79a6e 65%, #8a8682 100%); }
</style>
</head>
<body>
<div class="page">
  <div class="header-band"></div>
  <div class="header-rule"></div>
  <div class="flourish flourish--top" role="img" aria-label="Baroque leaf flourish ornament"></div>
  <div class="ribbon-stripes"></div>
  <div class="sidebar"></div>
  <div class="flourish flourish--bottom" role="img" aria-label="Baroque leaf flourish ornament"></div>

  <h1 class="page-title">Cakes</h1>

  <div class="brand-label">
    <p class="brand-name">Velvetrufflia</p>
  </div>

  <nav class="main-nav">
    <ul>
      <li><a href="#">Home</a></li>
      <li><a href="#">Cakes</a></li>
      <li><a href="#">Clients</a></li>
      <li><a href="#">Contact</a></li>
    </ul>
  </nav>

  <section class="cake-gallery">
    <div class="cake-photo cake-photo--fireside" role="img" aria-label="Chocolate-drip cream cake topped with strawberries before a fireplace"></div>
    <div class="cake-photo cake-photo--walnut" role="img" aria-label="Chocolate walnut torte with a slice removed"></div>
    <div class="cake-photo cake-photo--marzipan" role="img" aria-label="Domed marzipan cake with piped decoration and sugar rose"></div>
    <div class="cake-photo cake-photo--marzipan" role="img" aria-label="Domed marzipan cake with piped decoration and sugar rose"></div>
    <div class="cake-photo cake-photo--fireside" role="img" aria-label="Chocolate-drip cream cake topped with strawberries before a fireplace"></div>
    <div class="cake-photo cake-photo--layered" role="img" aria-label="Layered chocolate cake with a sugar rose, cut open"></div>
  </section>
</div>
</body>
</html>
```